まず、縦を想定しており、画像をメインにした構成を想定しております。

上半分は覚悟を決めた中年以上の料理にが仁王立ちしているようなイメージの写真で「店を売るという選択」or「店をゆずる決断」というキャプション

下半分はやる気に満ち溢れた若者が覚悟を持って仁王立ちしているようなイメージ
「店を買う」or「店(歴史)を引きつぐ覚悟」というキャプション

そして、下の方に計算式添付の資料にあるような表を挿入。
売却した方は結局、いくら得したのか。買った方はいくら得したのかがわかるように。あとは、「査定無料」「神奈川エリアに特化した唯一のエージェントです」を記載お願いします。最後にヴェルコハーバーズという社名と連絡先を記載。

全体的なイメージではノルヴェクや外国の広告のようにシンプルだけどもどこかデザイン性を感じるように。また、信頼性も大事なので全体的にシックだけども目を引くように。
VELKO HARBORS
ヴェルコハーバーズ
0120-471-362
www.velko-harbors-jp.example
A4
片面
青系、茶系、グレー系
• 高解像度JPG (.jpg)
• イラストレーター形式 (.ai)
キャプションの修正
【メインキャプション】大事なお店、最も高く売却いたします。
【売手側キャプション】 お店を売るという選択
【買手側キャプション】お店を買うという選択

また、各キャプションを大きめに表示をお願いします。

全体的にまとまっており、柔軟に対応頂いたため。

ありがとうござました!!

```html
<!DOCTYPE html>
<html lang="ja">
<head>
<meta charset="utf-8">
<title>ヴェルコハーバーズ 店舗売買</title>
<link rel="stylesheet" href="https://fonts.googleapis.com/css2?family=Noto+Sans+JP:wght@400;500;700;900&family=Noto+Serif+JP:wght@600;900&display=swap">
<style>
:root{
  --frame:#7fa7a6;
  --teal:#5f9e9a;
  --ink:#2b2b2b;
  --gray-dark:#5e605f;
  --pale:#e6ecea;
  --orange:#e08a2c;
  --white:#ffffff;
  --rule:#b9c6c4;
}
*{box-sizing:border-box;margin:0;padding:0}
html,body{width:874px;height:1200px;overflow:hidden;background:var(--white)}
body{font-family:"Noto Sans JP",sans-serif;color:var(--ink)}
.page{position:relative;width:874px;height:1200px;border:14px solid var(--frame);background:var(--white)}
.seller{position:absolute;left:16px;top:14px;width:814px;height:392px;background:linear-gradient(90deg,#9a9d9b,#7d807e 60%,#8a8d8b)}
.photo{position:absolute}
.seller .photo{left:140px;top:0;width:300px;height:392px;background:linear-gradient(180deg,#6b5f55,#4a4440 45%,#e9e9e7 46%,#f4f4f2)}
.buyer .photo{left:120px;top:0;width:300px;height:300px;background:linear-gradient(180deg,#6a4a32,#b89176 35%,#ebeae6 55%,#ffffff)}
.headline{position:absolute;font-family:"Noto Serif JP",serif;font-weight:900;line-height:0.95;white-space:nowrap}
.seller .headline{left:490px;top:20px;font-size:112px;color:var(--white)}
.sub{position:absolute;writing-mode:vertical-rl;font-family:"Noto Serif JP",serif;font-weight:600;font-size:26px;letter-spacing:4px;white-space:nowrap}
.seller .sub{left:736px;top:28px;color:var(--white)}
.note{position:absolute;font-size:11.5px;line-height:1.7}
.note .mark{display:block;font-size:24px;font-weight:900;line-height:1}
.seller .note{left:30px;top:120px;color:var(--white);width:100px}
.badge{position:absolute;left:672px;top:320px;width:100px;height:56px;background:var(--teal);color:var(--white);font-weight:700;font-size:21px;display:flex;align-items:center;justify-content:center;letter-spacing:2px}
.lead{position:absolute;left:16px;top:420px;width:814px;text-align:center;font-size:17px;font-weight:700;color:var(--teal)}
.buyer{position:absolute;left:16px;top:452px;width:814px;height:300px;background:linear-gradient(90deg,var(--pale),#f3f6f5)}
.buyer .headline{left:540px;top:40px;font-size:100px;color:var(--gray-dark)}
.buyer .sub{left:764px;top:40px;color:var(--gray-dark)}
.buyer .note{left:440px;top:70px;color:var(--gray-dark);width:90px}
.merit{position:absolute;left:16px;top:768px;width:814px;text-align:center;font-size:16px;font-weight:700;color:var(--orange)}
.brand{position:absolute;left:40px;top:860px;width:330px;text-align:center}
.brand-mark{display:flex;align-items:center;justify-content:center;gap:10px;margin-bottom:6px}
.brand-mark .dot{width:22px;height:22px;background:var(--teal)}
.brand-name{font-size:28px;font-weight:700;letter-spacing:1px;color:var(--gray-dark)}
.brand-kana{font-size:15px;font-weight:500;color:var(--gray-dark)}
.contact{position:absolute;left:24px;top:1030px;width:360px;font-weight:700;color:var(--ink)}
.contact .row{display:flex;align-items:center;gap:10px;padding:8px 0;border-top:1px solid var(--rule)}
.contact .label{font-size:12px;font-weight:500}
.contact .tel{font-size:27px;letter-spacing:1px}
.contact .url{font-size:16px}
.contact svg{flex:none}
.sim-label{position:absolute;left:392px;top:838px;writing-mode:vertical-rl;font-size:14px;font-weight:700;color:var(--gray-dark);letter-spacing:2px}
.sim{position:absolute;left:430px;top:830px;width:400px;font-size:12.5px}
.sim table{width:100%;border-collapse:collapse;margin-bottom:4px}
.sim th{font-weight:700;padding:3px 4px;text-align:center;border-bottom:1px solid var(--rule)}
.sim th.ours{color:var(--orange)}
.sim td{padding:4px;border-bottom:1px solid var(--rule);text-align:right}
.sim td:first-child{text-align:left}
.sim td.ours{color:var(--orange);font-weight:700}
.sim .total{background:var(--teal);color:var(--white);text-align:center;font-weight:700;font-size:15px;padding:4px 0;margin-bottom:16px}
</style>
</head>
<body>
<main class="page">
  <section class="seller">
    <div class="photo" role="img" aria-label="腕を組んで立つ料理人の男性の写真"></div>
    <p class="note"><span class="mark">!</span>長年守った店を手放す決断。その価値を正しく評価します。</p>
    <h1 class="headline">決<br>断。</h1>
    <p class="sub">店を売り出す</p>
    <div class="badge">査定無料</div>
  </section>

  <p class="lead">ヴェルコハーバーズは、神奈川エリアに特化した唯一の店舗売買エージェントです。</p>

  <section class="buyer">
    <div class="photo" role="img" aria-label="意欲に満ちた若い男性の写真"></div>
    <p class="note"><span class="mark">!</span>歴史ある店を引き継ぐ覚悟。新たな一歩を支えます。</p>
    <h2 class="headline">覚<br>悟。</h2>
    <p class="sub">店を引き継ぐ</p>
  </section>

  <p class="merit">お店を売却される方と買取りを希望される方の、双方にメリットが生まれる仕組みです。</p>

  <div class="brand">
    <div class="brand-mark"><span class="dot"></span><span class="brand-name">VELKO HARBORS</span></div>
    <div class="brand-kana">ヴェルコハーバーズ</div>
  </div>

  <div class="contact">
    <div class="row">
      <span class="label">お問合せは</span>
      <svg width="30" height="20" viewBox="0 0 30 20"><rect width="30" height="20" rx="4" fill="#2b2b2b"/><path d="M9 6a3 3 0 0 1 0 8M21 6a3 3 0 0 0 0 8" stroke="#fff" stroke-width="2.4" fill="none"/></svg>
      <span class="tel">0120-471-362</span>
    </div>
    <div class="row">
      <span class="label">URL</span>
      <svg width="12" height="14" viewBox="0 0 12 14"><path d="M2 1l9 6-9 6z" fill="#2b2b2b"/></svg>
      <span class="url">www.velko-harbors-jp.example</span>
    </div>
  </div>

  <p class="sim-label">売却・買取コストシミュレーション</p>

  <div class="sim">
    <table>
      <tr><th></th><th>通常閉店</th><th class="ours">弊社サービス</th></tr>
      <tr><td>解約前予納家賃</td><td>▲45 万円</td><td class="ours">0 円</td></tr>
      <tr><td>内装解体費用</td><td>▲55 万円</td><td class="ours">0 円</td></tr>
      <tr><td>造作譲渡代金</td><td>―</td><td class="ours">200 万円</td></tr>
      <tr><td>計</td><td>▲100 万円</td><td class="ours">200 万円</td></tr>
    </table>
    <div class="total">300 万円のメリット</div>
    <table>
      <tr><th></th><th>通常出店</th><th class="ours">弊社サービス</th></tr>
      <tr><td>内装設備投資額</td><td>1,300 万円</td><td class="ours">0 円</td></tr>
      <tr><td>造作代金</td><td>0 円</td><td class="ours">350 万円</td></tr>
      <tr><td>計</td><td>1,300 万円</td><td class="ours">350 万円</td></tr>
    </table>
    <div class="total">950 万円のコストダウン</div>
  </div>
</main>
</body>
</html>
```